Accounting & Tax Services in Edmonton, Canada-Needs Website Design & Improvement

I am starting my business for accounting and tax services in Canada. I have my website but not much happy with that. My services are for bookkeeping, accounting and tax services. We serve both individual and corporate clients. I am trying to bring new idea in the market for providing services at their facility or business. My existing website is www.qrmt.ca
Currently, this site is static but I want to improve it to dynamic or interactive in nature.

Target Market(s)

Edmonton and Surrounding Areas, Canada

Industry/Entity Type

Public Accounting

Logo Text

Harborline Ledger & Advisory Partners

Number of Pages Required

4 page

Font styles to use
Sans Serif

Colors

Designer to choose colors to be used in the design.

Requirements
Must have
• 4 Pages
• I a not sure what do we mean by coded and uncoded design. Need clarification
• Rest is explained in project description. It should have the ingredients to attract traffic in any professional website.
• Logo Design Text can be shortened, if required.
• Existing logo attached, just for reference.
Nice to have
• 5 Pages

```html
<!DOCTYPE html>
<html lang="en">
<head>
<meta charset="utf-8">
<title>Harborline Ledger &amp; Advisory Partners</title>
<link href="https://fonts.googleapis.com/css2?family=Crimson+Text:ital,wght@0,400;0,600;0,700;1,400&family=Lato:wght@400;700;900&family=Roboto:ital,wght@0,400;0,500;1,400&display=swap" rel="stylesheet">
<style>
:root{
  --navy:#1e5574;
  --band:#2a5f7c;
  --teal:#4a93a6;
  --teal-dark:#2d6a87;
  --ink:#333;
  --muted:#8a8f94;
  --charcoal:#2a2c2f;
  --white:#fff;
  --serif:"Crimson Text", Georgia, serif;
  --sans:"Roboto", Arial, sans-serif;
  --display:"Lato", Arial, sans-serif;
}
*{box-sizing:border-box;margin:0;padding:0}
html,body{width:1200px;height:3103px;overflow:hidden}
body{position:relative;font-family:var(--sans);color:var(--ink);background:var(--white)}
.abs{position:absolute}
.serif{font-family:var(--serif)}

/* top bar + header */
.topbar{left:0;top:0;width:1200px;height:46px;background:var(--band)}
.topbar .contact-item{top:13px;color:var(--white);font-size:15px;display:flex;align-items:center;gap:10px}
.header{left:0;top:46px;width:1200px;height:88px;background:var(--white)}
.brand{left:74px;top:20px;height:126px;width:260px;background:var(--white)}
.brand-name{left:78px;top:64px;font-family:var(--serif);font-size:25px;font-weight:600;color:var(--navy);line-height:1.05}
.brand-dot{left:78px;top:30px;width:24px;height:24px;border-radius:50%;background:var(--teal)}
.nav{left:385px;top:82px;display:flex;gap:0;font-size:15px;color:var(--teal-dark)}
.nav span{position:absolute;white-space:nowrap}
.nav .active{color:var(--navy)}

/* hero */
.hero{left:0;top:134px;width:1200px;height:569px;background:linear-gradient(90deg,#9aa6b0 0%,#7d8d99 30%,#54606a 60%,#3b4650 100%)}
.hero-title{right:78px;top:292px;text-align:right;color:var(--white);font-family:var(--display);font-weight:900;font-size:52px;line-height:1;text-shadow:0 2px 4px rgba(0,0,0,.35)}
.hero-sub{right:78px;top:355px;text-align:right;color:var(--white);font-family:var(--display);font-weight:700;font-size:36px}
.hero-text{right:78px;top:424px;width:560px;text-align:right;color:var(--white);font-size:15px;line-height:23px}
.btn{display:flex;align-items:center;justify-content:center;background:var(--white);color:var(--ink);font-size:17px;text-transform:uppercase}
.hero-btn{left:904px;top:517px;width:218px;height:46px}
.arrow{width:50px;height:50px;border-radius:50%;display:flex;align-items:center;justify-content:center;font-size:26px}
.arrow-prev{left:12px;top:368px;background:var(--white);color:var(--navy)}
.arrow-next{left:1138px;top:368px;background:var(--band);color:var(--white)}

/* welcome */
.welcome-title{left:0;width:1200px;top:698px;text-align:center;color:var(--white);font-family:var(--serif);font-size:50px}
.welcome-text{left:150px;width:900px;top:780px;text-align:center;color:#9fb9c7;font-size:14px;line-height:22px}
.welcome-btn{left:507px;top:869px;width:186px;height:46px}

/* callout */
.callout-title{left:78px;top:1012px;font-family:var(--serif);font-weight:700;font-size:44px;color:var(--navy)}
.callout-sub{left:80px;top:1062px;font-size:19px;color:var(--muted)}
.request-btn{left:674px;top:1030px;width:195px;height:50px;background:var(--teal);color:var(--white);font-size:18px}
.or{left:884px;top:1046px;font-size:13px;color:#b9c4ca}
.call-title{left:920px;top:1012px;font-family:var(--serif);font-weight:700;font-size:44px;color:var(--navy)}
.call-number{left:921px;top:1060px;font-family:var(--serif);font-size:25px;color:var(--navy)}

/* services */
.services{left:0;top:1140px;width:1200px;height:552px;background:linear-gradient(180deg,#2f3134,#1f2123)}
.section-title{left:0;width:1200px;text-align:center;font-family:var(--serif);font-size:50px}
.card-img{top:1266px;width:338px;height:248px}
.card-body{top:1514px;width:338px;height:125px;text-align:center;color:var(--white)}
.card-body h3{font-family:var(--serif);font-weight:400;font-size:30px;margin-top:12px}
.card-body p{font-size:14px;line-height:22px;color:#bfd6de;margin:6px 40px 0}
.c1{left:78px}.c2{left:430px}.c3{left:782px}
.card-body.c1,.card-body.c3{background:var(--teal)}
.card-body.c2{background:var(--teal-dark)}

/* testimonial */
.avatar{left:550px;top:1821px;width:100px;height:100px;border-radius:50%;border:3px solid var(--navy);background:radial-gradient(circle at 50% 40%,#e6c9a8,#b98a5e)}
.quote-mark{font-family:var(--serif);font-size:110px;color:#d7dadd;line-height:1}
.quote-text{left:190px;width:820px;top:1934px;text-align:center;font-style:italic;font-size:14.5px;line-height:23px;color:#555}
.quote-name{left:0;width:1200px;top:2012px;text-align:center;font-family:var(--serif);font-weight:700;font-size:24px;color:var(--navy)}

/* tax alert + contact */
.contact-bg{left:0;top:2110px;width:1200px;height:745px;background:linear-gradient(180deg,#2a2c2f,#1d1f21)}
.alert-date{font-family:var(--serif);font-size:52px;line-height:1;color:rgba(255,255,255,.28)}
.alert-month{font-size:13px;color:rgba(255,255,255,.4)}
.alert-text{font-size:14px;line-height:22px;color:#b9cfda;width:230px}
.alert-text.featured{font-family:var(--serif);font-weight:700;font-size:15px;color:var(--white);text-decoration:underline}
.divider{width:2px;height:70px;background:rgba(255,255,255,.15);transform:skewX(-15deg)}
.contact-text{left:260px;width:680px;top:2543px;text-align:center;color:var(--white);font-size:14px;line-height:23px}
.field{border:1.5px solid #ddd;color:var(--white);font-size:14px;padding:8px 12px}
.submit{left:505px;top:2756px;width:188px;height:46px;font-size:18px}

/* footer */
.footer{left:0;top:2855px;width:1200px;height:248px;background:var(--band)}
.fnav{top:2883px;font-size:14.5px;color:var(--white)}
.fnav.home{color:#9db4c1}
.social{width:46px;height:46px;border-radius:50%;border:2px solid var(--white);background:rgba(255,255,255,.08);top:2870px}
.rule{left:78px;top:2930px;width:1044px;height:1px;background:rgba(255,255,255,.3)}
.f-name{left:110px;top:2953px;font-family:var(--serif);font-weight:700;font-size:15px;color:var(--white)}
.f-addr{left:110px;top:2982px;font-size:12.5px;line-height:19px;color:var(--white)}
.f-line{font-size:15px;color:var(--white);display:flex;align-items:center;gap:12px}
.copyright{left:0;width:1200px;top:3060px;text-align:center;font-size:14px;color:#9db4c1}
.copyright b{color:var(--white);font-weight:500}
</style>
</head>
<body>

<!-- Top bar -->
<div class="abs topbar">
  <div class="abs contact-item" style="left:724px">
    <svg width="18" height="13" viewBox="0 0 18 13"><rect x="0.5" y="0.5" width="17" height="12" fill="#d6e2e9"/><path d="M0.5 0.5 9 7 17.5 0.5" fill="none" stroke="#2a5f7c" stroke-width="1.4"/></svg>
    hello@qrmt.ca
  </div>
  <div class="abs contact-item" style="left:986px">
    <svg width="12" height="18" viewBox="0 0 12 18"><rect x="0.5" y="0.5" width="11" height="17" rx="2" fill="#d6e2e9"/><rect x="2" y="2.5" width="8" height="11" fill="#2a5f7c"/></svg>
    (587) 555 0142
  </div>
</div>

<!-- Header -->
<div class="abs header"></div>
<div class="abs brand"></div>
<div class="abs brand-dot"></div>
<div class="abs brand-name">Harborline Ledger<br>&amp; Advisory Partners</div>
<nav class="abs nav">
  <span class="active" style="left:0">HOME</span>
  <span style="left:68px">FIRM PROFILE</span>
  <span style="left:190px">SERVICES</span>
  <span style="left:277px">NEWSLETTER</span>
  <span style="left:391px">FINANCIAL TOOLS</span>
  <span style="left:536px">INFO CENTER</span>
  <span style="left:650px">CONTACT US</span>
</nav>

<!-- Hero -->
<div class="abs hero" role="img" aria-label="Photo of a smiling businessman in a light suit talking on a phone, seated outdoors"></div>
<div class="abs hero-title">Harborline Ledger</div>
<div class="abs hero-sub">&amp; Advisory Partners</div>
<p class="abs hero-text">At Harborline Ledger &amp; Advisory Partners, we work hard to realize our motto. We view every client relationship like a partnership, and truly believe that our success is a result of your success.</p>
<div class="abs btn hero-btn">Get a free quote</div>
<div class="abs arrow arrow-prev">&laquo;</div>
<div class="abs arrow arrow-next">&raquo;</div>

<!-- Welcome band -->
<svg class="abs" style="left:0;top:612px" width="1200" height="354" viewBox="0 0 1200 354">
  <polygon points="0,91 600,8 1200,91 1200,354 0,354" fill="#2a5f7c"/>
  <polyline points="0,91 600,8 1200,91" fill="none" stroke="#fff" stroke-width="3"/>
</svg>
<h1 class="abs welcome-title" style="font-weight:400">Welcome To Harborline Ledger</h1>
<p class="abs welcome-text">Welcome and thank you for visiting our website. At Harborline Ledger &amp; Advisory Partners, we have built our business so that it guarantees your success. In addition to providing you with a profile of our firm and the services we provide, this website has been designed to become a helpful resource tool to you, our valued clients and visitors.</p>
<div class="abs btn welcome-btn">Read more</div>

<!-- Callout -->
<h2 class="abs callout-title">Want To Know More?</h2>
<p class="abs callout-sub">Request for a call back &nbsp;for get solution today...</p>
<div class="abs btn request-btn">Request now</div>
<div class="abs or">OR</div>
<h2 class="abs call-title">Call Now:</h2>
<div class="abs call-number">(587) 555 0142</div>

<!-- Services -->
<div class="abs services" role="img" aria-label="Dark background photo of a desk with keyboard and office items"></div>
<h2 class="abs section-title" style="top:1180px;color:#fff;font-weight:400">Our Services</h2>
<div class="abs card-img c1" role="img" aria-label="Photo of a hand writing on financial charts beside a calculator" style="background:linear-gradient(135deg,#f2f4f6,#c9d3dc)"></div>
<div class="abs card-img c2" role="img" aria-label="Photo of hands using a calculator and tablet over paperwork" style="background:linear-gradient(135deg,#e9edf0,#b7c2cb)"></div>
<div class="abs card-img c3" role="img" aria-label="Photo of a tax return form on a desk with a keyboard and mouse" style="background:linear-gradient(135deg,#eef0f2,#a9b6c2)"></div>
<div class="abs card-body c1"><h3>Bookkeeping</h3><p>Lorem Ipsum is simply dummy text of the printing and typesetting industry.</p></div>
<div class="abs card-body c2"><h3>Accounting</h3><p>Lorem Ipsum is simply dummy text of the printing and typesetting industry.</p></div>
<div class="abs card-body c3"><h3>Tax</h3><p>Lorem Ipsum is simply dummy text of the printing and typesetting industry.</p></div>

<!-- Testimonial -->
<h2 class="abs section-title" style="top:1734px;color:var(--navy);font-weight:400;font-size:48px">Testimonial</h2>
<div class="abs avatar" role="img" aria-label="Portrait photo of the client giving the testimonial"></div>
<div class="abs quote-mark" style="left:120px;top:1905px">&ldquo;</div>
<div class="abs quote-mark" style="left:1030px;top:1905px">&rdquo;</div>
<p class="abs quote-text">"Lorem ipsum dolor sit amet, consectetur adipiscing elit, sed do eiusmod tempor incididunt ut labore et dolore magna aliqua. Ut enim ad minim veniam, quis nostrud exercitation ullamco laboris nisi ut aliquip ex ea commodo consequat Lorem ipsum dolor sit amet, consectetur adipiscing elit, sed do eiusmod tempor incididunt ut labore et dolore magna aliqua."</p>
<div class="abs quote-name">- Lorem ipsum</div>

<!-- Tax alert + Contact -->
<div class="abs contact-bg" role="img" aria-label="Dark background photo of financial documents and a pen"></div>
<svg class="abs" style="left:0;top:2110px" width="1200" height="312" viewBox="0 0 1200 312">
  <polygon points="0,0 1200,0 1200,228 600,308 0,228" fill="#2a5f7c"/>
  <polyline points="0,228 600,308 1200,228" fill="none" stroke="#fff" stroke-width="3"/>
</svg>
<h2 class="abs section-title" style="top:2148px;color:#fff;font-weight:400">Tax Alert</h2>

<div class="abs alert-date" style="left:78px;top:2226px">16</div>
<div class="abs alert-month" style="left:86px;top:2278px">Nov</div>
<div class="abs divider" style="left:150px;top:2228px"></div>
<div class="abs alert-text featured" style="left:168px;top:2238px">AB - Changes made to political contributions tax credit</div>

<div class="abs alert-date" style="left:441px;top:2226px">16</div>
<div class="abs alert-month" style="left:449px;top:2278px">Nov</div>
<div class="abs divider" style="left:512px;top:2228px"></div>
<div class="abs alert-text" style="left:530px;top:2238px">AB - Changes made to political contributions tax credit</div>

<div class="abs alert-date" style="left:803px;top:2226px">16</div>
<div class="abs alert-month" style="left:811px;top:2278px">Nov</div>
<div class="abs divider" style="left:874px;top:2228px"></div>
<div class="abs alert-text" style="left:892px;top:2238px">AB - Changes made to political contributions tax credit</div>

<h2 class="abs section-title" style="top:2455px;color:#fff;font-weight:400">Contact Us</h2>
<p class="abs contact-text">Lorem Ipsum is simply dummy text of the printing and typesetting industry. Lorem Ipsum has been the industry's standard dummy text ever since the 1500s.</p>
<div class="abs field" style="left:265px;top:2603px;width:333px;height:37px">Name</div>
<div class="abs field" style="left:602px;top:2603px;width:333px;height:37px">Email Id</div>
<div class="abs field" style="left:265px;top:2646px;width:670px;height:102px">Comment</div>
<div class="abs btn submit">Submit</div>

<!-- Footer -->
<footer class="abs footer"></footer>
<span class="abs fnav home" style="left:78px">Home</span>
<span class="abs fnav" style="left:153px">Firm Profile</span>
<span class="abs fnav" style="left:261px">Services</span>
<span class="abs fnav" style="left:348px">Info Center</span>
<span class="abs fnav" style="left:453px">Financial Tools</span>
<span class="abs fnav" style="left:581px">Newsletter</span>
<span class="abs fnav" style="left:687px">Contact</span>
<div class="abs social" style="left:958px"></div>
<div class="abs social" style="left:1016px"></div>
<div class="abs social" style="left:1074px"></div>
<div class="abs rule"></div>

<svg class="abs" style="left:82px;top:2954px" width="14" height="20" viewBox="0 0 14 20"><path d="M7 0C3 0 0 3 0 7c0 5 7 13 7 13s7-8 7-13c0-4-3-7-7-7z" fill="#fff"/><circle cx="7" cy="7" r="2.6" fill="#2a5f7c"/></svg>
<div class="abs f-name">Harborline Ledger &amp; Advisory Partners</div>
<div class="abs f-addr">Northgate Commerce Centre<br>Suite 410-10200 108 St NW<br>Edmonton, AB T5J 1K3</div>

<div class="abs f-line" style="left:452px;top:2953px">
  <svg width="18" height="18" viewBox="0 0 18 18"><path d="M4 1l3 4-2 2c1 2 3 4 5 5l2-2 4 3-2 3C8 16 2 10 1 4z" fill="#fff"/></svg>
  (587) 555 0142
</div>
<div class="abs f-line" style="left:452px;top:2984px">
  <svg width="18" height="18" viewBox="0 0 18 18"><rect x="1" y="6" width="16" height="10" rx="1" fill="#fff"/><rect x="4" y="1" width="10" height="6" fill="#fff"/><rect x="5" y="9" width="8" height="2" fill="#2a5f7c"/></svg>
  (587) 555 0187
</div>
<div class="abs f-line" style="left:817px;top:2953px">
  <svg width="18" height="13" viewBox="0 0 18 13"><rect x="0.5" y="0.5" width="17" height="12" fill="#fff"/><path d="M0.5 0.5 9 7 17.5 0.5" fill="none" stroke="#2a5f7c" stroke-width="1.4"/></svg>
  hello@qrmt.ca
</div>
<div class="abs f-line" style="left:817px;top:2984px">
  <svg width="18" height="18" viewBox="0 0 18 18"><circle cx="9" cy="9" r="8" fill="#fff"/><path d="M1 9h16M9 1c-4 4-4 12 0 16M9 1c4 4 4 12 0 16" fill="none" stroke="#2a5f7c" stroke-width="1.2"/></svg>
  www.qrmt.ca
</div>
<div class="abs copyright">&copy; <b>Harborline Ledger &amp; Advisory Partners</b> &nbsp;2017. All Rights Reserved.</div>

</body>
</html>
```